Clearwave Motion Florida Billboard

We need a billboard designed for our physical therapy practice. Our billboard also serves as the sign for our building. We would like to have some sort of graphic notifying people driving by that our building is located here. Please go to www.clearwavemotionfl.example in order to get a better idea of our company.

Target Market(s)

Senior citizens having physical therapy

Industry/Entity Type

Healthcare- Physical Therapy

Colors
0094D4
00A9DD
6FCCEA
C7EBF8
E9F6FB

Requirements
Must have
• Must contain in bold the words "physical therapy". Must be highly visible from the road and have our company colors incorporated. Would also like to use the phrase "Relieving Pain. Restoring Function. Improving Lives."

```html
<!DOCTYPE html>
<html lang="en">
<head>
<meta charset="utf-8">
<title>Clearwave Motion Florida – Physical Therapy Billboard</title>
<link rel="stylesheet" href="https://fonts.googleapis.com/css2?family=Montserrat:wght@500;600&family=Oswald:wght@500;600&display=swap">
<style>
  :root {
    --page-bg: #f2f2f2;
    --brand-blue: #0094d4;
    --brand-sky: #00a9dd;
    --brand-light: #6fccea;
    --brand-pale: #c7ebf8;
    --accent-green: #8cc63f;
    --ink: #111111;
    --ink-soft: #333333;
    --white: #ffffff;
  }
  html, body {
    margin: 0;
    padding: 0;
    width: 1200px;
    height: 1200px;
    overflow: hidden;
    background: var(--page-bg);
  }
  .canvas {
    width: 1200px;
    height: 1200px;
    display: flex;
    align-items: center;
    justify-content: center;
  }
  .billboard {
    width: 1140px;
    height: 378px;
    display: block;
  }
  .brand-name { font-family: "Montserrat", sans-serif; font-weight: 500; fill: var(--ink-soft); letter-spacing: 1px; }
  .headline { font-family: "Oswald", sans-serif; font-weight: 600; fill: var(--brand-blue); }
  .tagline { font-family: "Oswald", sans-serif; font-weight: 500; fill: var(--ink); }
  .call-line { font-family: "Oswald", sans-serif; font-weight: 500; fill: var(--brand-blue); }
  .web-address { font-family: "Montserrat", sans-serif; font-weight: 600; fill: var(--white); letter-spacing: 1.6px; }
</style>
</head>
<body>
<main class="canvas">
  <svg class="billboard" viewBox="0 0 964 320" xmlns="http://www.w3.org/2000/svg" aria-label="Clearwave Motion Florida physical therapy billboard">
    <defs>
      <linearGradient id="photo-tones" x1="0" y1="0" x2="1" y2="1">
        <stop offset="0" stop-color="#e9eef0"/>
        <stop offset="0.45" stop-color="#9fc9dd"/>
        <stop offset="0.75" stop-color="#7fcfa6"/>
        <stop offset="1" stop-color="#b9bfc4"/>
      </linearGradient>
    </defs>

    <rect class="board-bg" x="0" y="0" width="964" height="320" fill="var(--white)"/>

    <path class="photo-area" role="img" aria-label="Photo: physical therapist in a blue polo working with a patient's leg resting on an exercise ball in a clinic"
          d="M628,0 H964 V320 H640 Q558,160 628,0 Z" fill="url(#photo-tones)"/>
    <path class="accent-arc" d="M610,0 H628 Q558,160 640,320 H628 Q538,160 610,0 Z" fill="var(--accent-green)"/>

    <path class="footer-band" d="M0,278 H612 L634,320 H0 Z" fill="var(--brand-blue)"/>

    <g class="brand-lockup">
      <circle cx="171" cy="59" r="40" fill="var(--brand-sky)"/>
      <text class="brand-name" x="232" y="46" font-size="24">CLEARWAVE</text>
      <text class="brand-name" x="232" y="74" font-size="24">MOTION</text>
      <text class="brand-name" x="232" y="93" font-size="13">FLORIDA</text>
    </g>

    <text class="headline" x="50" y="175" font-size="72" textLength="472" lengthAdjust="spacingAndGlyphs">PHYSICAL THERAPY</text>

    <g class="taglines">
      <text class="tagline" x="50" y="204" font-size="17">RELIEVING PAIN</text>
      <text class="tagline" x="200" y="204" font-size="17">RESTORING FUNCTION</text>
      <text class="tagline" x="522" y="204" font-size="17" text-anchor="end">IMPROVING LIVES</text>
    </g>

    <text class="call-line" x="302" y="261" font-size="36" text-anchor="middle">CALL : 555- 014- 2290</text>

    <text class="web-address" x="300" y="305" font-size="15" text-anchor="middle">WWW.CLEARWAVEMOTIONFL.EXAMPLE</text>
  </svg>
</main>
</body>
</html>
```